Design for 3.31” x 84” vinyl banner for tradeshow

Hello, I am looking for a design that will be printed on a 33.31” x 84” vinyl banner for my company’s tradeshow booth.

-Design

My vision: I want to give you the full background, because I think it’ll help. We design insulation for electronic tools that go in high temperature oilwells. Interestingly, a lot of the electronic tools that go down these oil wells are also used in geothermal wells. However the electronics would melt in these high temperature geothermal wells if they were not insulated. A lot of companies that make tools for the oil market are trying to re-purpose their existing tools for the geothermal market…..and to do this, they would need our insulation.

So, our sign needs to conveys this message: Trying to enter the geothermal logging market? it's as simple as increasing the temp. rating for your existing tools

This sign will be placed at our company’s booth at an industry tradeshow. The sign needs to have a similar style to our existing signs. I’ve included images of our booth and all of our other signs. This sign doesn’t have to be identical in artistic style, but be fairly similar.

-Art Requirements:

At least 1 Image of RBT logo

I’ve included several different variations. Use your judgement to select the one that you think is most fitting.

Do not use the portion of the logo that says “40 years”. Feel free to crop that out if you would like.

At least 2 images of logging tools. You can select more than 2 if you think that’s necessary. Logging tools are the long metal tubes.

I’ve included several pictures of different logging tools. I would like to see at least 2 pictures of tools on the banner. Please include the image titled “Full, double centarlizer” It could look cool if this picture extended the full length of the banner (just a suggestion). I purchased these images off of picvaultly.For the second image of the tool, feel free to include whatever tool you think looks best.

-Colors and font: Like I mentioned above, I would like it to look close to the other signs we have at our booth. Please select colors and fonts that will fit with our other signs.

-Other thoughts/suggestions

When most people in our industry think of geothermal, the automatically associate it with extremely high temperatures. I’m open to seeing warmer colors (orange/red) that help convey this idea.

I’m also open to seeing pictures of geothermal power plants, I included an image of this titled “geothermal” that you may use if you like. This is not mandatory, just a suggestion.

-Text: the main text needs to be: “Trying to enter the Geothermal logging market? Ask us about increasing the temperature rating for your existing tools” No other text is required.

Printing/Art specifications:

I’ll be giving the design I receive off art-huddle to a local banner printing shop. I’ve included their printing and art guidelines, please take a look at it and let me know if you have any questions. It’s pretty detailed so I hope it provides you with enough information. The design would have to follow the requirements in the two attached word documents.

Target Market(s)

oil and gas professionals

Industry/Entity Type

oil and gas/geothermal

Font styles to use
Other font styles liked:
• Fonts similar the font used on our other tradeshow signs (images attached)

Colors
F0912C
F2A743
F7CA91
FBE8D2
FDF5EE

Requirements
Must have
• -At least 1 Image of RBT logo, At least 2 images of logging tools (1 of these 2 pictures must be image titled "full double centralizer", he main text needs to be: “Trying to enter the Geothermal logging market? Ask us about increasing the temperature rating for your existing tools” , the design must follow the requirements in the printing and art guideline documents I attached.
Nice to have
• please select colors and fonts that will fit with our other signs.

```html
<!DOCTYPE html>
<html lang="en">
<head>
<meta charset="utf-8">
<title>Ridgeback Thermal – Geothermal Banner</title>
<link href="https://fonts.googleapis.com/css2?family=Oswald:wght@600;700&family=Montserrat:wght@600;700;800&display=swap" rel="stylesheet">
<style>
  :root {
    --brand-orange: #E9782B;
    --ink: #1E1E1E;
    --paper: #FFFFFF;
    --paper-shade: #EBEBEB;
    --backdrop: #A3A3A3;
    --steel-light: #C9C9C9;
    --steel-dark: #6E6E6E;
  }
  * { margin: 0; padding: 0; box-sizing: border-box; }
  html, body { width: 1200px; height: 923px; overflow: hidden; }
  body { background: var(--backdrop); position: relative; }

  .banner {
    position: absolute; left: 435px; top: 46px;
    width: 330px; height: 831px; overflow: hidden;
    background: linear-gradient(180deg, var(--paper) 0%, #F6F6F6 40%, var(--paper-shade) 80%);
    box-shadow: 0 8px 24px rgba(0,0,0,.35);
  }

  .brand {
    position: absolute; left: 0; right: 0; top: 50px;
    display: flex; align-items: center; justify-content: center; gap: 10px;
  }
  .brand-mark { width: 26px; height: 26px; background: var(--ink); }
  .brand-name {
    font-family: 'Oswald', sans-serif; font-weight: 700; color: var(--ink);
    font-size: 28px; line-height: 1.05; text-transform: uppercase;
  }

  .headline-lead {
    position: absolute; left: 0; right: 0; top: 136px; text-align: center;
    font-family: 'Oswald', sans-serif; font-weight: 700; font-size: 22px;
    line-height: 24px; color: var(--ink); letter-spacing: .3px;
  }
  .headline-band {
    position: absolute; left: 25px; top: 164px; width: 280px; height: 45px;
    background: var(--brand-orange);
    clip-path: polygon(0 10%, 4% 0, 100% 0, 100% 75%, 94% 100%, 0 100%);
    display: flex; align-items: center; justify-content: center;
    font-family: 'Oswald', sans-serif; font-weight: 700; font-size: 38px;
    line-height: 1; color: var(--paper); letter-spacing: .5px;
  }
  .headline-tail {
    position: absolute; left: 25px; width: 280px; top: 210px; text-align: center;
    font-family: 'Oswald', sans-serif; font-weight: 700; font-size: 36px;
    line-height: 40px; color: var(--brand-orange); white-space: nowrap;
  }

  .ground-band {
    position: absolute; left: 0; right: 0; top: 693px; bottom: 0;
    background: var(--ink); border-top: 4px solid var(--brand-orange);
  }

  .tool-photo { position: absolute; border-radius: 3px; }
  .tool-slim {
    left: 57px; top: 254px; width: 12px; height: 512px;
    background: linear-gradient(90deg, #B9B9B9, #7E7E7E 60%, #9A9A9A);
  }
  .tool-centralizer {
    left: 88px; top: 290px; width: 100px; height: 492px;
    background: linear-gradient(90deg, var(--steel-light) 0%, var(--steel-dark) 55%, #8A8A8A 100%);
    opacity: .85;
  }

  .vertical {
    position: absolute; writing-mode: vertical-rl; transform: rotate(180deg);
    white-space: nowrap;
  }
  .cta-ask {
    left: 204px; top: 344px; height: 170px; text-align: center;
    font-family: 'Montserrat', sans-serif; font-weight: 800; font-size: 42px;
    color: var(--brand-orange); line-height: 1;
  }
  .cta-detail {
    left: 250px; top: 266px; height: 326px; text-align: end;
    font-family: 'Montserrat', sans-serif; font-weight: 600; font-size: 16.5px;
    color: var(--ink); line-height: 22px;
  }

  .web-strip {
    position: absolute; left: 253px; top: 583px; width: 47px; bottom: 0;
    background: var(--brand-orange);
    clip-path: polygon(0 6%, 100% 0, 100% 100%, 0 100%);
  }
  .web-address {
    left: 266px; top: 622px; height: 142px; text-align: center;
    font-family: 'Montserrat', sans-serif; font-weight: 600; font-size: 12.5px;
    color: var(--paper);
  }
</style>
</head>
<body>
  <main class="banner">
    <div class="brand">
      <span class="brand-mark"></span>
      <span class="brand-name">Ridgeback<br>Thermal, Inc.</span>
    </div>

    <p class="headline-lead">TRYING TO ENTER THE</p>
    <div class="headline-band">GEOTHERMAL</div>
    <p class="headline-tail">LOGGING MARKET?</p>

    <div class="ground-band"></div>

    <div class="tool-photo tool-slim" role="img" aria-label="Photograph of a thin metal well logging tool with two small centralizers, standing upright"></div>
    <div class="tool-photo tool-centralizer" role="img" aria-label="Photograph of a full double centralizer logging tool, standing upright"></div>

    <p class="vertical cta-ask">Ask Us</p>
    <p class="vertical cta-detail">about increasing the temperature<br>rating for your existing tools</p>

    <div class="web-strip"></div>
    <p class="vertical web-address">RidgebackThermal.com</p>
  </main>
</body>
</html>
```